Etiketten für Getränkehersteller- und händler
Zielgruppe
Wir sind Getränkehersteller- und händler. Für unsere Partner haben wir exklusive Eigenmarken, die nur unserer Partner verkaufen. Der Sonnenrebe ist eine exklusive Gastronomiemarke, die nicht im Handel erhältlich ist. Leichter, gut-trinkbarer, mainstreamiger Sommerwein, für jede Art von Gastronomie. Den Wein gibt es im 3. Jahr.
Wir planen für die Zukunft, neben dem Weißwein die Produktrange um einen Rot-und Roséwein zu erweitern.
Aufgabenstellung
Arbeiten mit dem Logo/Etikett
1) Sonnenrebe-Schriftzug ist angemeldete Wort-Bild-Marke
2) Sonnenrebe soll weiterhin nummeriert werden (nächster Wein #4 Weisswein,)
3) Liquit steht erst zu einem späteren Zeitpunkt fest und kann daher beliebig für den Entwurf ausgewählt werden.
4) Darstellung des Etiketts auf der Flasche (siehe Anhang)
Was wir uns wünschen:
Alternative 1: Weiterentwicklung der Etiketten
1) Layout der Etiketten auf bestehender Designvorlage (weißwein, Rotwein, Rosé) mit neuem Farbcode weiterentwickeln
2) Etikettendesigns für die Sonnenreben #4 (2018), #5 (2019), #6 (2020)
Alternative 2: Modifizierung der Etiketten
1) Weiterentwicklung des bestehenden Etikettendesigns mit einem hohen Wiedererkennungswert zum heutigen Design
2) Anpassung des Logos in anderen Farben möglich, aber nicht zwingen
3) mehrere Ideen-Vorschläge gerne gesehen, muss aber nur für die 3 Sorten für das Jahr 2019 aufgezeigt werden
Farbgestaltung
1) Rotwein in rötlichen Tönen, gedeckte eher winterliche Farben
2) Rosé in rosa-Nuancen, helle Farben
3) Weißwein in hellen Sommerfarben (gelb,orange, sommerlich)
Infos zu Etikettenqualität und Flasche
Papier: Klebeetikett mit gestrichenem Papier
Flasche: Klarglasflasche für Weiß/Roséwein; Grün/Braunglas für Rotwein

```html
<!DOCTYPE html>
<html lang="de">
<head>
<meta charset="utf-8">
<title>Sonnenrebe #4 – #6 Etiketten</title>
<link rel="stylesheet" href="https://fonts.googleapis.com/css2?family=Antonio:wght@400;600;700&display=swap">
<style>
  :root {
    --bg: #ffffff;
    --panel: #ffffff;
    --brand-grey: #626262;
    --crimson: #c8004b;
    --rose: #e889ad;

    --peach-light: #fdd5c5;
    --peach-mid: #f6a285;
    --peach-edge: #c9a395;
    --orange: #f05a1e;

    --lilac-light: #dccae4;
    --lilac-mid: #b99bcb;
    --lilac-edge: #a596ac;
    --purple: #7c2e91;

    --sage-light: #cfe0da;
    --sage-mid: #9dbfb3;
    --sage-edge: #98a9a3;
    --green: #2d6f55;
  }

  * { box-sizing: border-box; margin: 0; padding: 0; }

  html, body {
    width: 1200px;
    height: 960px;
    overflow: hidden;
    background: var(--bg);
  }

  .label-row {
    position: relative;
    width: 1200px;
    height: 960px;
    display: flex;
    justify-content: center;
    align-items: center;
    gap: 70px;
  }

  .label {
    --tone-light: var(--peach-light);
    --tone-mid: var(--peach-mid);
    --tone-edge: var(--peach-edge);
    --accent: var(--orange);
    width: 280px;
    height: 350px;
    display: grid;
    grid-template-columns: 45px 2px 98px 2px 133px;
    font-family: "Antonio", "Arial Narrow", sans-serif;
  }

  .label--2019 {
    --tone-light: var(--lilac-light);
    --tone-mid: var(--lilac-mid);
    --tone-edge: var(--lilac-edge);
    --accent: var(--purple);
  }

  .label--2020 {
    --tone-light: var(--sage-light);
    --tone-mid: var(--sage-mid);
    --tone-edge: var(--sage-edge);
    --accent: var(--green);
  }

  .stripe-field {
    background: linear-gradient(
      180deg,
      var(--tone-light) 0%,
      var(--tone-mid) 18%,
      var(--crimson) 38%,
      var(--crimson) 56%,
      var(--rose) 68%,
      var(--tone-mid) 82%,
      var(--tone-light) 100%
    );
    opacity: 0.9;
  }

  .edge-line { background: var(--tone-edge); }

  .center-panel {
    background: var(--panel);
    display: flex;
    flex-direction: column;
    align-items: center;
    justify-content: space-between;
    padding: 14px 8px 14px;
  }

  .brand {
    width: 100%;
    text-align: center;
    color: var(--brand-grey);
  }

  .brand-name {
    font-weight: 700;
    font-size: 50px;
    line-height: 0.92;
    letter-spacing: -0.5px;
    text-transform: uppercase;
  }

  .brand-name span { display: block; }

  .edition {
    display: block;
    text-align: right;
    padding-right: 4px;
    font-weight: 600;
    font-size: 22px;
    line-height: 1;
    margin-top: 4px;
  }

  .edition small { font-size: 11px; font-weight: 400; }

  .wine-type {
    text-align: center;
    text-transform: uppercase;
    line-height: 0.95;
  }

  .wine-type span { display: block; }

  .wine-type .maker { color: var(--accent); font-weight: 600; font-size: 18px; }
  .wine-type .colour { color: var(--crimson); font-weight: 700; font-size: 38px; }
  .wine-type .kind { color: var(--rose); font-weight: 400; font-size: 30px; }
  .wine-type .vintage { color: var(--accent); font-weight: 700; font-size: 34px; }
</style>
</head>
<body>
<main class="label-row">

  <article class="label label--2018">
    <div class="stripe-field" role="img" aria-label="Gemalte Querstreifen in Pfirsich, Karminrot und Rosa"></div>
    <div class="edge-line"></div>
    <div class="center-panel">
      <div class="brand">
        <p class="brand-name"><span>Son</span><span>nen</span><span>rebe</span></p>
        <p class="edition"><small>#</small>4</p>
      </div>
      <p class="wine-type">
        <span class="maker">Muster</span>
        <span class="colour">Rot</span>
        <span class="kind">Wein</span>
        <span class="vintage">2018</span>
      </p>
    </div>
    <div class="edge-line"></div>
    <div class="stripe-field" role="img" aria-label="Gemalte Querstreifen in Pfirsich, Karminrot und Rosa"></div>
  </article>

  <article class="label label--2019">
    <div class="stripe-field" role="img" aria-label="Gemalte Querstreifen in Flieder, Karminrot und Rosa"></div>
    <div class="edge-line"></div>
    <div class="center-panel">
      <div class="brand">
        <p class="brand-name"><span>Son</span><span>nen</span><span>rebe</span></p>
        <p class="edition"><small>#</small>5</p>
      </div>
      <p class="wine-type">
        <span class="maker">Muster</span>
        <span class="colour">Rot</span>
        <span class="kind">Wein</span>
        <span class="vintage">2019</span>
      </p>
    </div>
    <div class="edge-line"></div>
    <div class="stripe-field" role="img" aria-label="Gemalte Querstreifen in Flieder, Karminrot und Rosa"></div>
  </article>

  <article class="label label--2020">
    <div class="stripe-field" role="img" aria-label="Gemalte Querstreifen in Salbeigrün, Karminrot und Rosa"></div>
    <div class="edge-line"></div>
    <div class="center-panel">
      <div class="brand">
        <p class="brand-name"><span>Son</span><span>nen</span><span>rebe</span></p>
        <p class="edition"><small>#</small>6</p>
      </div>
      <p class="wine-type">
        <span class="maker">Muster</span>
        <span class="colour">Rot</span>
        <span class="kind">Wein</span>
        <span class="vintage">2020</span>
      </p>
    </div>
    <div class="edge-line"></div>
    <div class="stripe-field" role="img" aria-label="Gemalte Querstreifen in Salbeigrün, Karminrot und Rosa"></div>
  </article>

</main>
</body>
</html>
```